Printing company needs a presentational catalogue, min. A5 format when closed, portrait or landscape

We need a corporate catalogue design for presentation of our company/services mainly to corporate customers. Our portfolio of services includes: offset printing, digital printing, screen printing, UV flatbed printing, direct UV printing on promotional items, textile printing (direct screen printing and heat transfer), computer cutting/plotting, CNC cutting, graphic design, setting for press; You can also use images of our products from our website www.lastovkabarve.si
We will adopt text later to the design so there should be some free space left for text. You should also determinate the typography of fonts for the category titles (offset printing, digital printing, etc...) and description of individual category.
Design should communicate in a way that we are there to solve our customer´s graphic problems and needs. Our new logo is attached. Catalogue colours should be matched with our new logo (kobalt lini). We will change our website soon (from lastovkabarve to kobaltlini), so the catalogue should not be in colours of existent website design (blue and orange).

Target Market(s)

B2B customers (mixed field of work)

Industry/Entity Type

Printing

Requirements
Must have
• Our new company logo, but it should not step out too much (better to be small and discreet).
Nice to have
• Some images of products that we offer - they could be from our website www.lastovkabarve.si if you can integrate them well into design...

```html
<!DOCTYPE html>
<html lang="sl">
<head>
<meta charset="utf-8">
<title>Kobalt Lini – katalog storitev</title>
<link rel="stylesheet" href="https://fonts.googleapis.com/css2?family=Kanit:wght@700&family=Poppins:wght@400;500;600;700&display=swap">
<style>
:root{
  --red:#d2232a;
  --red-dark:#b51c22;
  --ink:#2a2a2a;
  --text:#3d3d3d;
  --muted:#6b6b6b;
  --page:#eeeeee;
  --page-shade:#e2e2e2;
  --scene:#ececec;
}
*{box-sizing:border-box;margin:0;padding:0}
html,body{width:1200px;height:1031px;overflow:hidden;background:var(--scene);font-family:"Poppins",sans-serif;color:var(--text)}
.spread{position:absolute;left:40px;top:120px;width:1120px;height:792px;display:flex;box-shadow:0 12px 40px rgba(0,0,0,.18)}
.page{position:relative;width:560px;height:792px;overflow:hidden;
  background:linear-gradient(135deg,#f5f5f5 0%,var(--page) 40%,#f3f3f3 55%,var(--page-shade) 100%)}
.page--left{box-shadow:inset -14px 0 20px -14px rgba(0,0,0,.25)}
.page--right{box-shadow:inset 14px 0 20px -14px rgba(0,0,0,.25)}
.facets{position:absolute;inset:0;width:100%;height:100%}
.brand{position:absolute;top:28px;display:flex;align-items:center;gap:8px;font-weight:600;font-size:15px;letter-spacing:.04em;color:#555}
.brand__mark{width:20px;height:20px;border-radius:4px;background:var(--red)}
.page--left .brand{left:40px}
.page--right .brand{right:40px}
.year{position:absolute;top:32px;font-size:12px;font-weight:500;color:var(--ink)}
.page--left .year{right:28px}
.page--right .year{left:28px}
.rule{position:absolute;left:0;width:100%;height:60px}
.title{position:absolute;top:72px;font-family:"Kanit",sans-serif;font-weight:700;font-size:36px;color:var(--ink);letter-spacing:.01em}
.page--left .title{left:38px}
.page--right .title{right:38px}
.photo{position:absolute;top:126px;width:300px;height:210px;border:6px solid #fff;box-shadow:4px 8px 14px rgba(0,0,0,.3)}
.page--left .photo{left:32px;background:linear-gradient(135deg,#d9d9d9 0%,#b9986a 35%,#8a6a42 60%,#e4e4e4 100%)}
.page--right .photo{right:32px;background:linear-gradient(135deg,#d8dcdc 0%,#1f4e44 35%,#2c5f55 55%,#ecebe6 75%,#cfd3d3 100%)}
.checks{position:absolute;top:170px;list-style:none;display:flex;flex-direction:column;gap:10px;width:200px}
.page--left .checks{left:344px}
.page--right .checks{right:344px}
.check{display:flex;align-items:center;gap:10px;font-size:10.5px;font-weight:500;line-height:1.1;color:var(--ink);min-height:32px}
.page--right .check{flex-direction:row-reverse;justify-content:flex-start}
.check svg{flex:0 0 32px}
.body{position:absolute;top:360px;left:40px;right:40px;font-size:10.5px;line-height:1.35;color:var(--text)}
.body p{margin-bottom:11px}
.body strong{color:var(--ink);font-weight:700}
.features{position:absolute;left:40px;right:40px;display:grid;grid-template-columns:repeat(4,1fr);gap:3px 8px;list-style:none;font-size:8.5px;font-weight:500;color:var(--ink)}
.page--left .features{top:548px}
.page--right .features{top:602px}
.features li{display:flex;align-items:center;gap:5px}
.features li::before{content:"";width:0;height:0;border-left:7px solid var(--red);border-top:4px solid transparent;border-bottom:4px solid transparent;flex:0 0 auto}
.closing{position:absolute;top:622px;left:40px;right:40px;font-size:10.5px;line-height:1.35}
.footer{position:absolute;left:0;right:0;bottom:0;height:96px;background:linear-gradient(180deg,#d9d9d9,#cfcfcf);border-top:3px solid #fff;box-shadow:0 -1px 0 var(--red)}
.footer::after{content:"";position:absolute;left:0;right:0;bottom:0;height:6px;background:var(--red)}
.alert{position:absolute;top:26px;width:40px;height:40px;border:3px solid var(--red);border-radius:50%;display:flex;align-items:center;justify-content:center;color:var(--red);font-weight:700;font-size:22px;background:#f2f2f2}
.slogan{position:absolute;font-weight:700;font-size:11px;line-height:1.2;color:var(--ink);letter-spacing:.02em;text-transform:uppercase;white-space:nowrap}
.contact{position:absolute;top:-12px;width:200px;height:92px;background:var(--red);color:#fff;text-align:center;font-size:8.5px;line-height:1.5;padding-top:12px;font-style:normal}
.contact__name{font-weight:700;letter-spacing:.06em}
.page--left .alert{left:36px}
.page--left .slogan{left:88px;top:33px}
.page--left .contact{right:20px}
.page--right .alert{right:36px}
.page--right .slogan{right:88px;top:40px}
.page--right .contact{left:20px}
</style>
</head>
<body>
<main class="spread">

  <section class="page page--left">
    <svg class="facets" viewBox="0 0 560 792" preserveAspectRatio="none" aria-hidden="true">
      <polygon points="0,330 200,420 0,560" fill="#fff" opacity=".35"/>
      <polygon points="380,0 560,0 560,180" fill="#d8d8d8" opacity=".4"/>
      <polygon points="0,600 260,690 0,720" fill="#d4d4d4" opacity=".35"/>
    </svg>
    <div class="brand"><span class="brand__mark"></span>KOBALT LINI</div>
    <div class="year">2018.</div>
    <svg class="rule" style="top:36px" viewBox="0 0 560 60" preserveAspectRatio="none" aria-hidden="true">
      <path d="M170 22 Q360 6 560 40" stroke="var(--red)" stroke-width="2" fill="none"/>
    </svg>
    <h1 class="title">Digitalni tisk</h1>
    <svg class="rule" style="top:140px" viewBox="0 0 560 60" preserveAspectRatio="none" aria-hidden="true">
      <path d="M0 40 L300 30 Q430 22 560 30" stroke="var(--red)" stroke-width="2" fill="none"/>
    </svg>
    <div class="photo" role="img" aria-label="Fotografija potiskanih vizitk in ploščic v digitalnem tisku"></div>
    <ul class="checks">
      <li class="check"><svg width="32" height="32" viewBox="0 0 32 32" aria-hidden="true"><circle cx="16" cy="16" r="14" fill="#fff" stroke="var(--red)" stroke-width="3"/><path d="M10 16 l4 4 l8 -9" stroke="#444" stroke-width="2.5" fill="none" stroke-linecap="round"/></svg>Velika hitrost in fleksibilnost</li>
      <li class="check"><svg width="32" height="32" viewBox="0 0 32 32" aria-hidden="true"><circle cx="16" cy="16" r="14" fill="#fff" stroke="var(--red)" stroke-width="3"/><path d="M10 16 l4 4 l8 -9" stroke="#444" stroke-width="2.5" fill="none" stroke-linecap="round"/></svg>Možnost tiskanja na različne materiale</li>
      <li class="check"><svg width="32" height="32" viewBox="0 0 32 32" aria-hidden="true"><circle cx="16" cy="16" r="14" fill="#fff" stroke="var(--red)" stroke-width="3"/><path d="M10 16 l4 4 l8 -9" stroke="#444" stroke-width="2.5" fill="none" stroke-linecap="round"/></svg>Visoka kvaliteta in ločljivost tiska</li>
      <li class="check"><svg width="32" height="32" viewBox="0 0 32 32" aria-hidden="true"><circle cx="16" cy="16" r="14" fill="#fff" stroke="var(--red)" stroke-width="3"/><path d="M10 16 l4 4 l8 -9" stroke="#444" stroke-width="2.5" fill="none" stroke-linecap="round"/></svg>Cenovno ugoden pri manjših nakladah</li>
    </ul>
    <div class="body">
      <p><strong>Digitalno tiskanje</strong> je najhitrejša oblika izdelave različnih večbarvnih ali črno-belih tiskovin. Poleg tega je tudi ena izmed najugodnejših oblik tiska pri manjših nakladah. Pri digitalnem tisku namreč odpadejo zamudne priprave, saj se pričetek dela izvede neposredno iz računalnika oziroma datoteke.</p>
      <p>Glede na potrebe, uporabljamo 3 različne načine digitalnega tiska in sicer tisk s suhimi tonerji, solventni tisk ter Eco UV tisk.</p>
      <p>Tiskamo lahko na različne materiale v rolah in polah, prav tako pa nudimo tudi možnost potiska trdnih ploskovnih materialov (npr. aluminij, akril, Penex plošče, Trdex plošče, les,...).</p>
      <p>S pomočjo omenjenih barvnih digitalnih tehnologij tiska, vam lahko izdelamo široko paleto kvalitetnih in estetsko dovršenih izdelkov po vaših željah:</p>
    </div>
    <ul class="features">
      <li>Kataloge in prospekte</li>
      <li>POS oglaševalna stojala</li>
      <li>Plakate in letake</li>
      <li>Nalepke za talno in izložbeno grafiko</li>
      <li>Etikete na kolutu</li>
      <li>Prototipe unikatne embalaže</li>
      <li>Nalepke in etikete na polah</li>
      <li>Označevalne in informacijske table</li>
    </ul>
    <p class="closing">Zelo zanimiva in nova v naši ponudbi je kombinacija UV flatbed tiskalnika ter CNC rezalnika. Z njima lahko namreč ustvarjamo izdelke različnih oblik, ki so pravi lovilci pogledov in zato zelo primerni za oglaševalske akcije, sejme, razstave, muzeje, ipd.</p>
    <footer class="footer">
      <div class="alert">!</div>
      <p class="slogan">Hitro in fleksibilno z izjemnim<br>vizualnim učinkom</p>
      <address class="contact">
        <div class="contact__name">KOBALTLINI</div>
        Cvetlična ulica 14, 1000 Ljubljana - Vič<br>
        Tel.: 01/555 218 / Gsm: 040/555 734<br>
        E-mail: kobaltlini.si
      </address>
    </footer>
  </section>

  <section class="page page--right">
    <svg class="facets" viewBox="0 0 560 792" preserveAspectRatio="none" aria-hidden="true">
      <polygon points="560,0 400,0 560,160" fill="#d6d6d6" opacity=".45"/>
      <polygon points="0,520 220,700 0,720" fill="#fff" opacity=".3"/>
      <polygon points="560,420 360,560 560,600" fill="#dadada" opacity=".35"/>
    </svg>
    <div class="year">2018.</div>
    <div class="brand"><span class="brand__mark"></span>KOBALT LINI</div>
    <h1 class="title">Sitotisk/Industrijski sitotisk</h1>
    <svg class="rule" style="top:140px" viewBox="0 0 560 60" preserveAspectRatio="none" aria-hidden="true">
      <path d="M0 30 Q130 22 260 30 L560 40" stroke="var(--red)" stroke-width="2" fill="none"/>
    </svg>
    <div class="photo" role="img" aria-label="Fotografija zelene mape s sitotiskanim zlatim grbom in listino"></div>
    <ul class="checks">
      <li class="check"><svg width="32" height="32" viewBox="0 0 32 32" aria-hidden="true"><circle cx="16" cy="16" r="14" fill="#fff" stroke="var(--red)" stroke-width="3"/><path d="M10 16 l4 4 l8 -9" stroke="#444" stroke-width="2.5" fill="none" stroke-linecap="round"/></svg>Maksimalna oprijemljivost in obstojnost tiska</li>
      <li class="check"><svg width="32" height="32" viewBox="0 0 32 32" aria-hidden="true"><circle cx="16" cy="16" r="14" fill="#fff" stroke="var(--red)" stroke-width="3"/><path d="M10 16 l4 4 l8 -9" stroke="#444" stroke-width="2.5" fill="none" stroke-linecap="round"/></svg>Visoka pokrivnost in kvaliteta odtisov</li>
      <li class="check"><svg width="32" height="32" viewBox="0 0 32 32" aria-hidden="true"><circle cx="16" cy="16" r="14" fill="#fff" stroke="var(--red)" stroke-width="3"/><path d="M10 16 l4 4 l8 -9" stroke="#444" stroke-width="2.5" fill="none" stroke-linecap="round"/></svg>Odlična barvna reprodukcija</li>
      <li class="check"><svg width="32" height="32" viewBox="0 0 32 32" aria-hidden="true"><circle cx="16" cy="16" r="14" fill="#fff" stroke="var(--red)" stroke-width="3"/><path d="M10 16 l4 4 l8 -9" stroke="#444" stroke-width="2.5" fill="none" stroke-linecap="round"/></svg>Možnost doseganja posebnih učinkov ali zaščite</li>
    </ul>
    <div class="body">
      <p><strong>Sitotisk</strong> oz. <strong>grafični sitotisk</strong> je tradicionalna tiskarska tehnika, ki pa je z razvojem modernih strojev, najfinejših sitotiskarskih mrežic ter visokotehnoloških barv in premazov, marsikdaj prva izbira pri izvedbi najzahtevnejših tiskov. Omogoča ustvarjanje zelo ostrih in izjemno obstojnih eno ali večbarvnih motivov. Zelo pestra je tudi izbira materialov, saj lahko s to tehniko tiskamo na PVC folije, plastiko, akril, steklo, kovine, blago, les, usnje ter še na mnogo drugih umetnih in naravnih materialov.</p>
      <p>Poleg eno ali večbarvnega tiska na različne predmete, tiskamo tudi v tehniki »full-color« kar pomeni, da tiskani motivi v visoki ločljivosti dosegajo foto kvaliteto.</p>
      <p><strong>Industrijski sitotisk</strong> se od grafičnega razlikuje v tehnološki opremi, ki zaradi večje zmogljivosti strojev in avtomatiziranega procesa tiska ter sušenja, omogoča bistveno hitrejšo in zahtevnejšo proizvodnjo. Pri industrijskem sitotisku je večji poudarek na funkcionalnih lastnostih tiskarskih barv in premazov, saj morajo zadostiti najvišjim industrijskim standardom, kjer je zahtevana maksimalna odpornost na mehanske, fizikalne in kemijske vplive.</p>
    </div>
    <ul class="features">
      <li>PVC nalepke</li>
      <li>Tisk na tehnične materiale</li>
      <li>Tisk na akrilno steklo</li>
      <li>Potisk kartonske/plastične embalaže</li>
      <li>Tisk na aluminij</li>
      <li>Industrijske etikete</li>
      <li>UV premazi</li>
      <li>Tisk čelnih plošč aparatov</li>
    </ul>
    <footer class="footer">
      <address class="contact">
        <div class="contact__name">KOBALTLINI</div>
        Cvetlična ulica 14, 1000 Ljubljana - Vič<br>
        Tel.: 01/555 218 / Gsm: 040/555 734<br>
        E-mail: kobaltlini.si
      </address>
      <p class="slogan">Tisk za najzahtevnejše aplikacije</p>
      <div class="alert">!</div>
    </footer>
  </section>

</main>
</body>
</html>
```